Artist needs a business card for her pencil portraits and streetscapes

My mum is an artist and does fabulous portraits and sketches with pencil and needs a business card.
She likes designs that are a bit weird or unusual. The winning design will NOT be a slick modern corporate looking logo. It should be a little bit rustic and different. Interesting patterns and textures would be great, it doesn't even need to look like a business card! Come up with something unique!

Target Market(s)

Older clientele looking for family portraits

Industry/Entity Type

Artists

Contact Information for Business Card

Basically just need the name and contact details

Font styles to use
Decorative
Script

Requirements
Must have
• Lena Brodsworth
• Artist
• 0427913562
• lenabrodsworth@quillpost.example
Nice to have
• Weird artistic backgrounds, interesting textures, unusual designs for an artistic woman.
Should not have
• Nothing ultra modern and nothing corporate looking.

```html
<!DOCTYPE html>
<html lang="en">
<head>
<meta charset="utf-8">
<title>Lena Brodsworth – Artist Business Cards</title>
<link rel="stylesheet" href="https://fonts.googleapis.com/css2?family=Kaushan+Script&family=Open+Sans:wght@400;700&display=swap">
<style>
  :root {
    --page: #ffffff;
    --ink: #111111;
    --panel: #ffffff;
    --panel-edge: #c9c9c9;
    --pencil-light: #e6e6e6;
    --pencil-mid: #cfcfcf;
    --pencil-dark: #b9b9b9;
  }
  html, body {
    margin: 0;
    padding: 0;
    width: 1200px;
    height: 906px;
    overflow: hidden;
    background: var(--page);
  }
  .canvas {
    position: relative;
    width: 1200px;
    height: 906px;
    background: var(--page);
    color: var(--ink);
  }
  .card {
    position: absolute;
  }
  .card-texture {
    position: absolute;
    inset: 0;
    background:
      linear-gradient(90deg, transparent 0 44%, rgba(255,255,255,0.35) 47%, transparent 50% 100%),
      linear-gradient(180deg, var(--pencil-light) 0%, var(--pencil-mid) 35%, var(--pencil-light) 60%, var(--pencil-dark) 100%);
  }
  .card-panel {
    position: absolute;
    background: var(--panel);
    text-align: center;
  }
  .card--tall { left: 50px; top: 27px; width: 450px; height: 788px; }
  .card--tall .card-panel {
    left: 17px; top: 231px; width: 408px; height: 323px;
    border: 2px solid var(--panel-edge);
  }
  .card--short { left: 712px; top: 27px; width: 447px; height: 531px; }
  .card--short .card-panel { left: 18px; top: 28px; width: 414px; height: 465px; }

  .name, .phone {
    font-family: "Kaushan Script", cursive;
    margin: 0;
    line-height: 1;
  }
  .role, .email {
    font-family: "Open Sans", sans-serif;
    margin: 0;
    line-height: 1.1;
  }
  .card--tall .name { margin-top: 52px; font-size: 42px; }
  .card--tall .role { margin-top: 2px; font-size: 27px; }
  .card--tall .phone { margin-top: 68px; font-size: 36px; }
  .card--tall .email { margin-top: 4px; font-size: 21px; }

  .card--short .name { margin-top: 30px; font-size: 82px; line-height: 1.6; }
  .card--short .name span { display: block; }
  .card--short .name .name-last { font-size: 72px; }
  .card--short .role { margin-top: -12px; font-size: 27px; }
  .card--short .phone { margin-top: 64px; font-size: 36px; }
  .card--short .email { margin-top: 4px; font-size: 21px; }

  .variant-label {
    position: absolute;
    font-family: "Open Sans", sans-serif;
    font-weight: 700;
    font-size: 27px;
    transform: translateX(-50%);
    margin: 0;
  }
  .variant-label--a { left: 272px; top: 836px; }
  .variant-label--b { left: 930px; top: 576px; }
</style>
</head>
<body>
<main class="canvas">
  <section class="card card--tall">
    <div class="card-texture" role="img" aria-label="Grey hand-drawn pencil shading texture with soft vertical folds"></div>
    <div class="card-panel">
      <h1 class="name">Lena Brodsworth</h1>
      <p class="role">Artist</p>
      <p class="phone">0427913562</p>
      <p class="email">lenabrodsworth@quillpost.example</p>
    </div>
  </section>
  <p class="variant-label variant-label--a">A</p>

  <section class="card card--short">
    <div class="card-texture" role="img" aria-label="Grey hand-drawn pencil shading texture with soft vertical folds"></div>
    <div class="card-panel">
      <h2 class="name"><span>Lena</span><span class="name-last">Brodsworth</span></h2>
      <p class="role">Artist</p>
      <p class="phone">0427913562</p>
      <p class="email">lenabrodsworth@quillpost.example</p>
    </div>
  </section>
  <p class="variant-label variant-label--b">B</p>
</main>
</body>
</html>
```